KPL Business Card Design

I am attaching my logo and want both a black and white modern, contemporary card for my business.

Below are the details I require on the cards and of course I would need to be able to change this.

Thanks

Rob

Robert J Harcourt

Sales & Marketing Director

 

Vivid Panel Gazette

PO Box 4417

Chatham

Kent

ME7 5QX

 

Tel +44 (0) 1632 960 418

Mobile: +44 (0) 7700 900 537

Fax: +44 (0) 1632 960 772

Email: rob@vividpanelgazette.example

Website: www.vividpanelgazette.example

 

 

Be part of a World full of imagination,

knowledge and inspiration

 

 

Derek Pashley

Editorial Director

 

Vivid Panel Gazette

42 Fernhurst Close

Ashbury

Wessex

TW7 4LN

 

Tel: +44 (0) 208 496 0213

Mobile: +44 (0) 7700 900 864

Email: derek@vividpanelgazette.example

 

 

knowledge and inspiration

This is the same font as used in the logo.......

Robert J Harcourt

 

Vivid Panel Gazette

PO Box 4417

Chatham

Kent

ME7 5QX

 

Tel +44 (0) 1632 960 418

Fax: +44 (0) 1632 960 772

 

 

Derek Pashley

Editorial Director

 

Vivid Panel Gazette

42 Fernhurst Close

Ashbury

Wessex

TW7 4LN

 

Tel: +44 (0) 208 496 0213

Please add the following words to the back of the card and maybe add the logo to the back again.....

knowledge and inspiration

Robert J Harcourt

 

Vivid Panel Gazette

PO Box 4417

Chatham

Kent

ME7 5QX

 

Tel +44 (0) 1632 960 418

Fax: +44 (0) 1632 960 772

 

 

Derek Pashley

Editorial Director

 

Vivid Panel Gazette

42 Fernhurst Close

Ashbury

Wessex

TW7 4LN

 

Tel: +44 (0) 208 496 0213

knowledge and inspiration

Target Market(s)

Wide Format printing, Screen Printing, Digital Printing, Textile Printing, Signage, Digital Signage, Exhibition Graphics, Digital Textiles and more

Industry/Entity Type

Publishing

Requirements
Must have
• I would like to use these words on the back of the card both for a full black card and white card.

"Step into a World rich in creativity, insight and bright new ideas"

```html
<!DOCTYPE html>
<html lang="en">
<head>
<meta charset="utf-8">
<title>Vivid Panel Gazette – Business Cards</title>
<link rel="stylesheet" href="https://fonts.googleapis.com/css2?family=Nunito+Sans:wght@400;700&family=Arimo&display=swap">
<style>
  :root {
    --ink: #000;
    --paper: #fff;
    --orange: #f08a1e;
    --grey: #8a8a8a;
    --rule: #9a9a9a;
    --map-dark: #1b1b1b;
    --map-light: #f3f3f3;
  }
  * { margin: 0; padding: 0; box-sizing: border-box; }
  html, body { width: 1200px; height: 697px; overflow: hidden; background: var(--paper); }
  body { position: relative; font-family: "Nunito Sans", sans-serif; }

  .dimension-label { position: absolute; font-family: "Arimo", sans-serif; font-size: 19px; color: #111; }
  .dimension-label--width { left: 138px; top: 0; }
  .dimension-label--height { left: 0; top: 115px; }
  .dimension-line { position: absolute; background: var(--rule); }
  .dimension-line--width { left: 139px; top: 24px; width: 423px; height: 1.5px; }
  .dimension-line--height { left: 61px; top: 114px; width: 1.5px; height: 215px; }

  .card {
    position: absolute; width: 423px; height: 216px; border-radius: 108px;
    filter: drop-shadow(5px 6px 5px rgba(0,0,0,.35));
  }
  .card--black { background: var(--ink); color: var(--paper); }
  .card--white { background: var(--paper); color: var(--ink); }
  .card--front-black { left: 139px; top: 114px; }
  .card--front-white { left: 757px; top: 114px; }
  .card--back-black { left: 139px; top: 459px; }
  .card--back-white { left: 757px; top: 459px; }

  .logo-disc {
    position: absolute; left: 19px; top: 18px; width: 180px; height: 180px; border-radius: 50%;
    display: flex; align-items: center; justify-content: center; text-align: center;
  }
  .card--black .logo-disc { background: var(--paper); color: var(--ink); }
  .card--white .logo-disc { background: var(--ink); color: var(--paper); }
  .logo-name { font-weight: 700; font-size: 20px; line-height: 1.15; }

  .brace { position: absolute; left: 199px; top: 63px; width: 22px; height: 88px; }

  .contact { position: absolute; left: 226px; font-size: 11.5px; line-height: 14.2px; white-space: nowrap; }
  .contact--top { top: 27px; }
  .contact--bottom { top: 142px; }
  .contact-name { font-size: 14.5px; line-height: 17px; }
  .card--white .contact-muted { color: var(--grey); }
  .phone-key { display: inline-block; width: 16px; }
  .card--black .phone-key { color: var(--orange); }

  .world-map {
    position: absolute; left: 35px; top: 47px; width: 353px; height: 133px; border-radius: 20px;
  }
  .card--black .world-map { background: radial-gradient(ellipse at center, var(--map-dark), var(--ink) 75%); }
  .card--white .world-map { background: radial-gradient(ellipse at center, var(--map-light), var(--paper) 75%); }

  .tagline {
    position: absolute; left: 33px; top: 92px; font-size: 13px; line-height: 16.5px;
    letter-spacing: 1.3px; color: var(--orange); white-space: nowrap;
  }
  .tagline-line--second { display: block; padding-left: 86px; }
  .website {
    position: absolute; left: 0; right: 0; top: 188px; text-align: center; font-size: 13.5px;
  }
</style>
</head>
<body>
  <div class="dimension-label dimension-label--width">88mm</div>
  <div class="dimension-line dimension-line--width"></div>
  <div class="dimension-label dimension-label--height">45mm</div>
  <div class="dimension-line dimension-line--height"></div>

  <section class="card card--black card--front-black">
    <div class="logo-disc"><span class="logo-name">Vivid Panel<br>Gazette</span></div>
    <svg class="brace" viewBox="0 0 22 88"><path d="M20 2 Q10 2 10 12 V34 Q10 44 2 44 Q10 44 10 54 V76 Q10 86 20 86" fill="none" stroke="#fff" stroke-width="4"/></svg>
    <div class="contact contact--top">
      <div class="contact-name">Derek Pashley</div>
      <div>Managing Editor</div>
      <div>derek@vividpanelgazette.example</div>
    </div>
    <div class="contact contact--bottom">
      <div>42 Fernhurst Close, Ashbury,</div>
      <div>Wessex&nbsp; TW7 4LN</div>
      <div><span class="phone-key">T</span>: +44 (0) 208 496 0213</div>
      <div><span class="phone-key">M</span>: +44 (0) 7700 900 864</div>
    </div>
  </section>

  <section class="card card--white card--front-white">
    <div class="logo-disc"><span class="logo-name">Vivid Panel<br>Gazette</span></div>
    <svg class="brace" viewBox="0 0 22 88"><path d="M20 2 Q10 2 10 12 V34 Q10 44 2 44 Q10 44 10 54 V76 Q10 86 20 86" fill="none" stroke="#000" stroke-width="4"/></svg>
    <div class="contact contact--top">
      <div class="contact-name">Derek Pashley</div>
      <div class="contact-muted">Managing Editor</div>
      <div>derek@vividpanelgazette.example</div>
    </div>
    <div class="contact contact--bottom">
      <div class="contact-muted">42 Fernhurst Close, Ashbury,</div>
      <div class="contact-muted">Wessex&nbsp; TW7 4LN</div>
      <div><span class="phone-key">T</span>: +44 (0) 208 496 0213</div>
      <div><span class="phone-key">M</span>: +44 (0) 7700 900 864</div>
    </div>
  </section>

  <section class="card card--black card--back-black">
    <div class="world-map" role="img" aria-label="Faint outline map of the world"></div>
    <p class="tagline">Step into a World rich in<span class="tagline-line--second">creativity, insight and bright new ideas</span></p>
    <div class="website">www.vividpanelgazette.example</div>
  </section>

  <section class="card card--white card--back-white">
    <div class="world-map" role="img" aria-label="Faint outline map of the world"></div>
    <p class="tagline">Step into a World rich in<span class="tagline-line--second">creativity, insight and bright new ideas</span></p>
    <div class="website">www.vividpanelgazette.example</div>
  </section>
</body>
</html>
```